I need a business card design for my new clinic (ATHLETIC CARE OF JOINT). I am orthopedist, expert in sports surgery, especially knee surgery. I prefer, as colors, the colors of my logo (green, black and white). I already have my logo and should appear on my card. It's good to see my site to have ideas (www.drlucianovarela.example)
It needs contain:
my name: Dr. Luciano Varela
my registration: CRM 584-902
my specialty: Cirurgia do Joelho / Esporte
my address: Centro Empresarial - Parque Aurora Mall
Av. Doutor Augusto Valadares Pinto, 2740 sala 803
Jd. Acácias - Ribeirão Preto - SP
my phone number: Tel (16) 8420-5937
my clinic phone: (16) 3745-8081
my e-mail: drlucianovarela@mailbox.example
my site: www.drlucianovarela.example

Target Market(s)

futures patients

Industry/Entity Type

Clinic

Requirements
Nice to have
• letters not overfilled
straight lines, with few curves

```html
<!DOCTYPE html>
<html lang="pt-BR">
<head>
<meta charset="UTF-8">
<title>Athletic Care of Joint – Cartão de Visita</title>
<link rel="stylesheet" href="https://fonts.googleapis.com/css2?family=Questrial&display=swap">
<style>
  :root {
    --bg: #2a2c2f;
    --card: #ffffff;
    --green: #22a15a;
    --black: #0c0c0c;
    --ink: #1b1b1b;
    --grey: #5a5a5a;
    --rule: #b9b9b9;
  }
  * { box-sizing: border-box; margin: 0; padding: 0; }
  html, body { width: 1200px; height: 848px; overflow: hidden; }
  body {
    background: var(--bg);
    font-family: "Questrial", "Helvetica Neue", Arial, sans-serif;
    color: var(--ink);
    position: relative;
  }
  .card {
    position: absolute;
    width: 540px;
    height: 300px;
    background: var(--card);
    border-radius: 26px;
    overflow: hidden;
    top: 274px;
  }
  .card--front { left: 40px; }
  .card--back { left: 620px; }

  /* brand */
  .brand { position: absolute; display: flex; align-items: center; gap: 14px; }
  .brand__square { width: 74px; height: 74px; background: var(--black); border-radius: 8px; }
  .brand__name { font-size: 52px; letter-spacing: 2px; color: var(--black); line-height: 1; }

  /* front */
  .card--front .brand { left: 28px; top: 30px; }
  .front__rule { position: absolute; left: 118px; right: 20px; top: 118px; height: 1px; background: var(--rule); }
  .doctor { position: absolute; right: 40px; top: 130px; text-align: right; }
  .doctor__name { font-size: 26px; color: var(--ink); }
  .doctor__specialty { font-size: 16px; color: var(--grey); margin-top: 4px; }

  .contact { display: flex; align-items: center; gap: 6px; font-size: 15px; color: var(--grey); line-height: 1.5; }
  .contact svg { width: 16px; height: 16px; flex: none; }
  .contacts--left { position: absolute; left: 24px; top: 210px; border-top: 1px solid var(--rule); padding-top: 4px; width: 210px; }
  .contacts--right { position: absolute; left: 266px; top: 180px; }
  .contacts--right .contact { font-size: 14px; }

  .band { position: absolute; }
  .band--front-green { left: 0; bottom: 0; width: 252px; height: 34px; background: var(--green); }
  .band--front-black { left: 264px; right: 0; bottom: 0; height: 66px; background: var(--black); }

  /* back */
  .card--back .brand { left: 50%; transform: translateX(-50%); top: 30px; }
  .address { position: absolute; left: 0; right: 0; top: 124px; text-align: center; font-size: 14px; color: var(--grey); line-height: 1.45; }
  .site { position: absolute; left: 0; right: 0; top: 196px; text-align: center; font-size: 18px; letter-spacing: 1px; color: var(--green); }
  .band--back-black { left: 0; bottom: 0; width: 320px; height: 56px; background: var(--black); }
  .band--back-green { left: 332px; right: 0; bottom: 0; height: 34px; background: var(--green); }
</style>
</head>
<body>

<section class="card card--front" aria-label="Frente do cartão">
  <div class="brand">
    <span class="brand__square"></span>
    <span class="brand__name">VARELA</span>
  </div>
  <div class="front__rule"></div>

  <div class="doctor">
    <p class="doctor__name">Dr. Luciano Varela</p>
    <p class="doctor__specialty">Cirurgia do Joelho / Esporte</p>
  </div>

  <div class="contacts--right">
    <p class="contact">
      <svg viewBox="0 0 16 16" fill="none" stroke="#555" stroke-width="1.3"><rect x="2" y="2" width="12" height="12" rx="2"/><line x1="5" y1="6" x2="11" y2="6"/><line x1="5" y1="9" x2="11" y2="9"/><line x1="5" y1="12" x2="9" y2="12"/></svg>
      CRM 584-902
    </p>
    <p class="contact">
      <svg viewBox="0 0 16 16" fill="none" stroke="#555" stroke-width="1.3"><circle cx="8" cy="8" r="7"/><rect x="4" y="5.5" width="8" height="5.5"/><polyline points="4,5.5 8,8.5 12,5.5"/></svg>
      drlucianovarela@mailbox.example
    </p>
  </div>

  <div class="contacts--left">
    <p class="contact">
      <svg viewBox="0 0 16 16" fill="none" stroke="#555" stroke-width="1.3"><circle cx="8" cy="8" r="7"/><path d="M5.5 4.5l1.5 1.5-1 1.2c.6 1.2 1.4 2 2.6 2.6l1.2-1 1.5 1.5-1 1.2c-2.6-.4-4.8-2.6-5.2-5.2z"/></svg>
      (16) 3745-8081
    </p>
    <p class="contact">
      <svg viewBox="0 0 16 16" fill="none" stroke="#555" stroke-width="1.3"><circle cx="8" cy="8" r="7"/><rect x="5.5" y="3.5" width="5" height="9" rx="1"/><line x1="7" y1="11" x2="9" y2="11"/></svg>
      (16) 8420-5937
    </p>
  </div>

  <div class="band band--front-green"></div>
  <div class="band band--front-black"></div>
</section>

<section class="card card--back" aria-label="Verso do cartão">
  <div class="brand">
    <span class="brand__square"></span>
    <span class="brand__name">VARELA</span>
  </div>
  <p class="address">
    Centro Empresarial - Parque Aurora Mall<br>
    Av. Doutor Augusto Valadares Pinto, 2740 sala 803<br>
    Jd. Acácias - Ribeirão Preto - SP
  </p>
  <p class="site">www.drlucianovarela.example</p>
  <div class="band band--back-black"></div>
  <div class="band band--back-green"></div>
</section>

</body>
</html>
```